Merrow Lodge - Boutique lodge in the Canadian Rockies

We need to re-do our website.
It is old and looks terrible.
www.merrowlodge-example.com
We are in the process of upgrading the property, so the website needs to reflect a 4.5 star boutique mountain property. Rustic luxury. Attached is the new rooms decor concept.
Target Market(s)
skiing, snowboarding, hiking, Adventure, outdoors, couples.
Industry/Entity Type
Hotel
Logo Text
Merrow Lodge
Coding
Coded - Design and coding required
Number of Pages Required
5+ page
Requirements
Must have
- Luxury, canadian rocky mountain theme.
Should not have
- Cowboy theme.

```html
<!DOCTYPE html>
<html lang="en">
<head>
<meta charset="utf-8">
<title>Merrow Lodge – Website Presentation</title>
<link href="https://fonts.googleapis.com/css2?family=Montserrat:wght@400;600;700&family=Hind:wght@300;400;500&display=swap" rel="stylesheet">
<style>
:root{
  --board:#e9eaec;
  --page:#ffffff;
  --dark:#2b2b2b;
  --darker:#232323;
  --nav:rgba(40,40,40,.78);
  --beige:#d9d7c3;
  --brown:#9a7750;
  --navy:#3b4b6e;
  --gold:#e6c219;
  --ink:#2f2f2f;
  --muted:#7a7a7a;
  --rule:#d4d4d4;
}
*{box-sizing:border-box;margin:0;padding:0}
html,body{width:1200px;height:1200px;overflow:hidden;background:var(--board)}
body{position:relative;font-family:"Hind",sans-serif;color:var(--ink)}
.abs{position:absolute}
.page{position:absolute;background:var(--page);overflow:hidden;box-shadow:0 1px 4px rgba(0,0,0,.25)}
.page--home{left:69px;top:37px;width:535px;height:1127px}
.page--rooms{left:627px;top:38px;width:535px;height:1046px}
.topbar{position:absolute;left:0;top:0;width:100%;height:14px;background:var(--darker);color:#aaa;font-size:4px;line:14px;display:flex;align-items:center;justify-content:space-between;padding:0 60px}
.topbar span{margin-left:8px}
.nav{position:absolute;left:0;width:100%;height:29px;background:var(--nav);display:flex;align-items:center;padding-left:62px}
.logo{display:flex;align-items:center;gap:4px;color:#fff;font-family:"Montserrat",sans-serif;font-weight:700;font-size:7.5px;letter-spacing:.3px;width:120px}
.logo i{display:block;width:8px;height:8px;border-radius:50%;background:#c9b27f}
.nav ul{list-style:none;display:flex;height:100%}
.nav li{color:#fff;font-family:"Montserrat",sans-serif;font-size:4.2px;font-weight:600;padding:0 7px;display:flex;align-items:center}
.nav li.on{background:#fff;color:var(--ink)}
.photo{position:absolute}
.h-serif{font-family:"Montserrat",sans-serif;font-weight:700;color:var(--ink)}
.small{font-size:4.2px;line-height:8.4px;color:#555}
.btn-out{position:absolute;border:1px solid var(--ink);font-size:4px;font-family:"Montserrat",sans-serif;padding:3px 8px;background:#fff}
.btn-brown{position:absolute;background:var(--brown);color:#fff;font-size:3.8px;font-family:"Montserrat",sans-serif;padding:3px 7px}
.rule{position:absolute;left:0;width:100%;height:1px;background:var(--rule)}
.room-title{position:absolute;font-family:"Montserrat",sans-serif;font-weight:700;font-size:11.5px;line-height:12.5px;color:#3a3a3a}
.from{position:absolute;font-size:4.2px;color:#555;letter-spacing:.2px}
.desc{position:absolute;font-size:4.1px;line-height:8.3px;color:#555;width:125px}
.overlay{position:absolute;left:388px;top:666px;width:501px;height:510px;background:rgba(28,28,28,.9);color:#fff;padding:34px 30px 0 36px;font-size:13.4px;line-height:17.2px;font-weight:300}
.overlay p{margin-bottom:17px}
.overlay a{color:var(--gold);text-decoration:none}
</style>
</head>
<body>

<!-- HOME PAGE -->
<section class="page page--home">
  <div class="topbar"><div>42 Larch Bend, P.O. Box 7, BC Canada V0A 2B0 &nbsp; Lodge/Spa (250) 555-0148</div><div><span>ABOUT</span><span>SUITES</span><span>THE SPA</span><span>THE RIDGEBACK SALOON</span></div></div>
  <div class="photo" role="img" aria-label="Timber-frame lodge exterior among tall pines under a blue sky" style="left:0;top:14px;width:535px;height:277px;background:linear-gradient(180deg,#5b86c0 0%,#a9c4e2 28%,#5f7a4f 55%,#5a3a24 78%,#4a3626 100%)"></div>
  <div class="nav" style="top:14px"><div class="logo"><i></i>MERROW LODGE</div><ul><li class="on">WELCOME</li><li>SUITES ▾</li><li>THE SPA</li><li>THE RIDGEBACK SALOON</li><li>ACTIVITIES</li><li>GALLERY</li><li>CONTACT ▾</li></ul></div>
  <svg class="abs" style="left:12px;top:143px" width="10" height="14"><path d="M8 1 2 7l6 6" fill="none" stroke="#fff" stroke-width="1.4"/></svg>
  <svg class="abs" style="left:513px;top:143px" width="10" height="14"><path d="M2 1l6 6-6 6" fill="none" stroke="#fff" stroke-width="1.4"/></svg>
  <div class="nav" style="top:251px;height:40px;background:rgba(45,45,45,.85)"><div class="logo"><i></i>MERROW LODGE</div><ul><li class="on">WELCOME</li><li>SUITES ▾</li><li>THE SPA</li><li>THE RIDGEBACK SALOON</li><li>ACTIVITIES</li><li class="on">GALLERY</li><li>CONTACT ▾</li></ul></div>

  <div class="abs" style="left:0;top:291px;width:535px;height:40px;background:var(--beige)">
    <div class="abs" style="left:61px;top:15px;color:#fff;font-family:Montserrat,sans-serif;font-weight:700;font-size:7px">CHECK AVAILABILITY</div>
    <div class="abs" style="left:167px;top:12px;width:62px;height:14px;border:1px solid #fff;color:#fff;font-size:3.6px;padding:4px">Arrival Date</div>
    <div class="abs" style="left:236px;top:12px;width:62px;height:14px;border:1px solid #fff;color:#fff;font-size:3.6px;padding:4px">Departure Date</div>
    <div class="abs" style="left:305px;top:12px;width:42px;height:14px;border:1px solid #fff;color:#fff;font-size:3.6px;padding:4px">Adult</div>
    <div class="abs" style="left:360px;top:12px;width:35px;height:14px;border:1px solid #fff;color:#fff;font-size:3.6px;padding:4px">Children</div>
    <div class="btn-brown" style="left:405px;top:12px;height:14px;padding-top:4px">CHECK AVAILABILITY</div>
  </div>

  <div class="photo" role="img" aria-label="Bright twin guest room with grey curtains" style="left:70px;top:343px;width:184px;height:177px;background:linear-gradient(160deg,#e8e8e6,#b9bcbd 55%,#6e6f70)"></div>
  <h2 class="abs h-serif" style="left:284px;top:350px;width:180px;text-align:center;font-size:11px">Merrow Lodge</h2>
  <p class="abs small" style="left:274px;top:375px;width:200px;text-align:center">Merrow Lodge &amp; Spa opened in December 2005 offering luxurious, ski-in accommodation, steps from the heart of the resort and gondola, and at the hub of the resort's 2,750 acres of skiing. Eleven unique suites provide an intimate, relaxing environment, allying a traditional rustic charm and coziness, reminiscent of the Great National Park Lodges, with modern comforts.</p>
  <div class="btn-out" style="left:330px;top:434px">LEARN MORE ABOUT THE SUITES</div>
  <p class="abs small" style="left:274px;top:461px;width:200px;text-align:center">One of the principal focal points of Merrow Lodge is the Great Room, with a floor to ceiling stone fireplace where you are destined to relax and sip a glass of wine, or enjoy the beautiful view of the Canadian Rockies.</p>
  <div class="btn-out" style="left:326px;top:501px">LEARN MORE ABOUT THE AMENITIES</div>
  <div class="rule" style="top:511px"></div>

  <h2 class="abs h-serif" style="left:100px;top:560px;width:124px;text-align:center;font-size:11px">Guest Rooms</h2>
  <p class="abs" style="left:61px;top:587px;font-size:4.2px;font-weight:500">All of our suites have:</p>
  <ul class="abs small" style="left:70px;top:599px;list-style:disc;line-height:12px;padding-left:4px">
    <li>Private balconies, with stunning views</li><li>En-suite bathroom</li><li>Some rooms have jacuzzi tubs for 2 over looking the Rocky Mountains</li><li>Goose down duvet and feather bed</li><li>Heated Floors</li>
  </ul>
  <svg class="abs" style="left:68px;top:676px" width="280" height="40" font-family="Hind" font-size="4" fill="#777">
    <g fill="none" stroke="#cfc6a8" stroke-width="1"><circle cx="15" cy="10" r="9"/><path d="M10 9a7 7 0 0 1 10 0M12 11a4 4 0 0 1 6 0"/><rect x="62" y="5" width="16" height="11" rx="2"/><circle cx="66" cy="17" r="2"/><circle cx="74" cy="17" r="2"/><path d="M110 8h20M113 8v8h14V8M120 3v5"/><rect x="163" y="4" width="20" height="13"/><path d="M168 1l5 3 5-3"/></g>
    <text x="4" y="36">Free Wifi</text><text x="57" y="36">Car Parking</text><text x="108" y="36">Room Service</text><text x="160" y="36">Flat screen TV</text>
  </svg>
  <div class="photo" role="img" aria-label="Cedar-panelled guest room with ceiling lamp" style="left:282px;top:558px;width:184px;height:162px;background:linear-gradient(170deg,#8a6a4e,#b07d4f 45%,#5e3f29)"></div>
  <div class="rule" style="top:771px"></div>
  <h2 class="abs h-serif" style="left:150px;top:768px;width:235px;text-align:center;font-size:11px;background:#fff">ACCOMMODATIONS</h2>
  <p class="abs small" style="left:170px;top:787px;width:195px;text-align:center">It is a long established fact that a reader will be distracted by the readable content of a page when looking at its layout</p>

  <div class="photo" role="img" aria-label="Platinum suite with twin beds" style="left:61px;top:818px;width:130px;height:115px;background:linear-gradient(160deg,#7d5a3d,#c39a6c 50%,#6a4a32)"></div>
  <div class="abs" style="left:61px;top:933px;width:130px;height:38px;background:var(--navy);text-align:center;padding-top:7px"><div style="color:#fff;font-family:Montserrat,sans-serif;font-size:8.6px">PLATINUM (VIP) SUITE</div><div style="color:var(--gold);font-size:4.2px;font-weight:500;margin-top:4px">START FROM $295.00 PER DAY</div></div>
  <div class="photo" role="img" aria-label="Golden room with wooden bed" style="left:202px;top:818px;width:130px;height:115px;background:linear-gradient(160deg,#d8c8a6,#b8864f 50%,#6d4528)"></div>
  <div class="abs" style="left:202px;top:933px;width:130px;height:38px;background:var(--navy);text-align:center;padding-top:7px;white-space:nowrap"><div style="color:#fff;font-family:Montserrat,sans-serif;font-size:8.6px">GOLDEN (DELUXE) ROOMS</div><div style="color:var(--gold);font-size:4.2px;font-weight:500;margin-top:4px">START FROM $245.00 PER DAY</div></div>

  <div class="abs" style="left:0;top:1007px;width:535px;height:120px;background:var(--dark)">
    <div class="abs" style="left:0;top:25px;width:100%;height:1px;background:#3e3e3e"></div>
    <div class="abs" role="img" aria-label="Guest portrait" style="left:61px;top:44px;width:40px;height:40px;border-radius:50%;background:radial-gradient(#d9b79a,#8a6b55)"></div>
    <p class="abs" style="left:119px;top:56px;width:300px;font-size:4.2px;line-height:5.6px;color:#ddd">“ This is the only place to stay in Alder Ridge! I have stayed in the cheaper hotels and they were fine, but this is just the icing on the cake. After spending the day bike riding and hiking to come back and enjoy a glass of wine while looking out at the ocean, it all off.. ”</p>
    <div class="abs" style="left:119px;top:94px;width:3px;height:3px;border-radius:50%;background:#fff"></div>
    <div class="abs" style="left:124px;top:94px;width:3px;height:3px;border-radius:50%;background:#888"></div>
  </div>
</section>

<!-- ROOMS PAGE -->
<section class="page page--rooms">
  <div class="photo" role="img" aria-label="Guest room interior with framed pictures" style="left:0;top:0;width:535px;height:132px;background:linear-gradient(100deg,#dedcd6,#bfa888 50%,#9b8467)"></div>
  <div class="topbar" style="height:12px;background:var(--darker)"><div>42 Larch Bend, P.O. Box 7, BC Canada V0A 2B0 &nbsp; Lodge/Spa (250) 555-0148</div><div><span>ABOUT</span><span>SUITES</span><span>THE SPA</span><span>THE RIDGEBACK SALOON</span></div></div>
  <div class="nav" style="top:12px;height:30px"><div class="logo"><i></i>MERROW LODGE</div><ul><li>WELCOME</li><li class="on">SUITES ▾</li><li>THE SPA</li><li>THE RIDGEBACK SALOON</li><li>ACTIVITIES</li><li>GALLERY</li><li>CONTACT ▾</li></ul></div>
  <div class="abs h-serif" style="left:219px;top:76px;font-size:11px;color:#4a3a2a">ROOMS &amp; RATES</div>
  <div class="abs" style="left:224px;top:92px;font-size:4.5px;color:#fff">Lorem Ipsum is simply dummy text</div>

  <div class="rule" style="top:230px"></div>
  <div class="photo" role="img" aria-label="Platinum suite twin beds on timber frames" style="left:61px;top:145px;width:271px;height:211px;background:linear-gradient(160deg,#8a6242,#d4b48a 45%,#8f6a45 75%,#5b3f28)"></div>
  <div class="room-title" style="left:343px;top:200px">PLATINUM (VIP) SUITE</div>
  <div class="from" style="left:343px;top:220px">START FROM $295.00 PER DAY</div>
  <p class="desc" style="left:343px;top:236px">The VIP Suite offers guests a luxurious spacious apartment style accommodation spread over two floors with un compromised views across the mountain range. The comfortably styled sitting area is furnished with a love seat, coffee table and writing desk.</p>
  <div class="btn-brown" style="left:343px;top:292px">VIEW DETAILS</div>

  <div class="rule" style="top:472px"></div>
  <div class="photo" role="img" aria-label="Golden room with wooden sleigh bed" style="left:202px;top:392px;width:272px;height:194px;background:linear-gradient(160deg,#e2d3b2,#c29a63 45%,#8a5a33 80%,#6a3f25)"></div>
  <div class="room-title" style="left:61px;top:434px">GOLDEN (DELUXE)<br>ROOMS</div>
  <div class="from" style="left:61px;top:465px">START FROM $245.00 PER DAY</div>
  <p class="desc" style="left:61px;top:482px">Golden Rooms promise a comfortable and restful stay with a flexible choice of bed configurations: California Split king, Queen or Twin beds accommodating up to four guests if required. Golden Rooms' en-suite bathrooms offer a romantic extra deep Jacuzzi tub with spectacular mountains views.</p>
  <div class="btn-brown" style="left:61px;top:538px">VIEW DETAILS</div>

  <div class="rule" style="top:714px"></div>
  <div class="photo" role="img" aria-label="Silver room with wood panelling and balcony door" style="left:61px;top:622px;width:271px;height:182px;background:linear-gradient(160deg,#c8c5bd,#a9814f 50%,#7a5533)"></div>
  <div class="room-title" style="left:343px;top:658px">SILVER (STANDARD)<br>ROOMS</div>
  <div class="from" style="left:343px;top:690px">START FROM $195.00 PER DAY</div>
  <p class="desc" style="left:343px;top:706px">Silver Rooms promise a comfortable and restful stay with a choice of sleeping options: Daybed, Queen or a California split king that converts into 2 twins. The en-suite bathroom offers a walk-in shower or tub shower combination. Selected Silver Rooms are equipped for wheelchair access.</p>
  <div class="btn-brown" style="left:343px;top:762px">VIEW DETAILS</div>

  <div class="abs h-serif" style="left:89px;top:850px;font-size:7px;color:#555">Learn more about the Amenities</div>
  <div class="abs" style="left:272px;top:830px;width:202px;height:62px;border:1.5px solid #555">
    <div class="abs h-serif" style="left:10px;top:17px;font-size:7px;font-weight:600">Booking Policies</div>
    <div class="abs" style="left:140px;top:33px;border:1px solid #555;font-size:3.8px;padding:3px 6px">▪ Read More</div>
  </div>

  <div class="abs" style="left:0;top:904px;width:535px;height:29px;background:#3a3a3a">
    <div class="abs" style="left:80px;top:9px;color:#666;font-family:Montserrat,sans-serif;font-size:7px">NEWS &amp; OFFERS</div>
    <div class="abs" style="left:176px;top:8px;width:99px;height:13px;border:1px solid #777;font-size:3.5px;color:#aaa;padding:4px">your email</div>
    <div class="btn-brown" style="left:307px;top:8px;height:13px;padding:4px 12px">SIGN UP</div>
    <svg class="abs" style="left:376px;top:8px" width="92" height="14"><g fill="none" stroke="#ddd" stroke-width="1"><circle cx="7" cy="7" r="5.5"/><circle cx="25" cy="7" r="5.5"/><circle cx="43" cy="7" r="5.5"/><circle cx="61" cy="7" r="5.5"/><circle cx="79" cy="7" r="5.5"/></g></svg>
  </div>
  <div class="abs" style="left:0;top:933px;width:535px;height:113px;background:var(--dark)">
    <div class="abs" style="left:0;top:22px;width:100%;height:1px;background:#444"></div>
    <p class="abs" style="left:166px;top:14px;width:90px;font-size:3.6px;line-height:6.2px;color:#666">Merrow Lodge &amp; Spa opened in December 2005 offering luxurious, ski-in accommodation, steps from the heart of the resort and gondola, and at the hub of the resort's acres of skiing.</p>
    <div class="abs" style="left:272px;top:14px;color:#fff;font-family:Montserrat,sans-serif;font-weight:700;font-size:4.8px">MERROW LODGE</div>
    <div class="abs" style="left:272px;top:30px;font-size:3.9px;line-height:14px;color:#aaa">About<br>Suites<br>The SPA<br>The Ridgeback Saloon</div>
    <div class="abs" style="left:378px;top:14px;color:#fff;font-family:Montserrat,sans-serif;font-weight:700;font-size:4.8px">TRAILREVIEW</div>
    <div class="abs" style="left:378px;top:25px;width:100px;height:20px;background:#fff;border:1px solid #ccc">
      <div class="abs" style="left:3px;top:3px;width:14px;height:14px;background:#d9d9d9"></div>
      <div class="abs" style="left:28px;top:7px;font-size:4px;color:#333">Read 108 reviews of Merrow</div>
    </div>
    <div class="abs" style="left:503px;top:81px;width:22px;height:21px;background:var(--gold);color:#fff;font-size:9px;text-align:center;line-height:21px">↑</div>
    <svg class="abs" style="left:395px;top:104px" width="80" height="8"><g fill="#ccc"><rect x="0" y="1" width="14" height="5" rx="1"/><rect x="20" y="1" width="10" height="5" rx="2.5"/><rect x="36" y="1" width="14" height="5" rx="1"/><rect x="58" y="0" width="12" height="7" rx="1"/></g></svg>
  </div>
</section>

<!-- PRESENTATION NOTE -->
<aside class="overlay">
  <p>HELLO,<br>I want to present to you my work - Merrow Lodge website.<br>I hope you will like it.</p>
  <p>The websites' design is quite difficult to provide here - &nbsp;I have prepared the opportunity to analyze it live!</p>
  <p>You can check it by this address: &nbsp;<a href="#">merrow.demo-example.com</a></p>
  <p>Few words about website:<br>Fully responsive design ( adapted to mobile devices)<br>Easy to edit (popular Pressline CMS)<br>Site is included premium plugin for rooms booking ( you can test it on a site - I added your rooms and different prices (like your rates))<br>And many other possibilities to present your Lodge for customers.</p>
  <p>Please note: Not all images are with good resolution, so I added some placeholders.. Also I made a new LOGO, but if you dont like it &nbsp;- I'm ready to provide another revisions.</p>
  <p>Also, I offer my additional services: SEO (search engines optimization), menu designs, banners and slides design.<br>If you'll choose this design - I'll provide you full lifetime support.</p>
  <p>So, please check it here: <a href="#">merrow.demo-example.com</a> and I waiting your feedback</p>
</aside>

</body>
</html>
```